Small Business Consulting Firm Needs Business Card Design

Need a sleek modern business card with 2 sides matching the colors of our logo. We will be placing these with a mailer we are sending out. These business cards will only ever be given to business owners. We operate helping businesses who are struggling with cash flow or finances. If the green and blue design needs to be moved to the right of "Harborline Crest Consulting" for aesthetic purposes that is ok. We will need an editable file if possible. We would like to include the reps name, email, website, and phone number. For now just use Peter Vance, pvance@harborlinecrest.com, www.harborlinecrest.com, and 833-555-0172.

```html
<!DOCTYPE html>
<html lang="en">
<head>
<meta charset="utf-8">
<title>Harborline Crest Consulting — Business Card</title>
<link rel="stylesheet" href="https://fonts.googleapis.com/css2?family=Mulish:wght@300;400&display=swap">
<style>
  :root {
    --backdrop: #d8d2c8;
    --brand-blue: #0a7dc7;
    --deep-blue: #0d5b97;
    --brand-green: #6cbf44;
    --rich-green: #1d9a48;
    --paper: #eeeeee;
    --ink: #3a3a3a;
    --white: #ffffff;
  }
  * { margin: 0; padding: 0; box-sizing: border-box; }
  html, body { width: 900px; height: 1200px; overflow: hidden; }
  body {
    background: var(--backdrop);
    font-family: "Mulish", Arial, sans-serif;
    position: relative;
  }
  .card {
    position: absolute;
    left: 78px;
    width: 746px;
    height: 436px;
    box-shadow: 0 4px 10px rgba(0,0,0,0.35);
    overflow: hidden;
  }
  /* Front */
  .card-front { top: 134px; background: var(--brand-blue); color: var(--white); }
  .front-mark {
    position: absolute; left: 360px; top: 122px;
    width: 26px; height: 26px; background: var(--brand-green);
  }
  .front-company {
    position: absolute; left: 0; right: 0; top: 244px;
    text-align: center;
  }
  .front-company .company-name {
    display: block; font-size: 26px; font-weight: 400;
    letter-spacing: 2px; text-transform: uppercase;
  }
  .front-company .company-tagline {
    display: block; margin-top: 9px; padding-left: 120px;
    font-size: 13px; letter-spacing: 8px; text-transform: uppercase;
  }
  .front-web {
    position: absolute; left: 0; right: 0; top: 383px;
    text-align: center; font-size: 16px; letter-spacing: 4px; font-weight: 300;
  }
  .front-web .web-domain { color: var(--brand-green); }

  /* Back */
  .card-back { top: 637px; background: var(--paper); }
  .back-band {
    position: absolute; left: 0; right: 0; top: 236px; bottom: 0;
    background: linear-gradient(180deg, var(--brand-blue) 0%, var(--brand-blue) 60%, var(--deep-blue) 100%);
  }
  .rep {
    position: absolute; left: 51px; top: 70px;
  }
  .rep-name { font-size: 29px; font-weight: 400; color: var(--brand-blue); line-height: 1.1; }
  .rep-name .rep-surname { color: var(--brand-green); }
  .rep-title { font-size: 17px; color: var(--ink); margin-top: 2px; }
  .back-company {
    position: absolute; right: 66px; top: 72px; width: 170px;
    text-align: right; font-size: 22px; line-height: 1.25;
    font-weight: 400; color: var(--brand-green);
  }
  .contacts {
    position: absolute; left: 51px; top: 322px; list-style: none;
    color: var(--white); font-size: 17.5px; font-weight: 300;
  }
  .contacts li { display: flex; align-items: center; height: 21.5px; }
  .contacts svg { width: 13px; height: 13px; margin-right: 15px; fill: var(--brand-green); }
</style>
</head>
<body>

<section class="card card-front">
  <div class="front-mark"></div>
  <div class="front-company">
    <span class="company-name">Harborline Crest</span>
    <span class="company-tagline">Consulting</span>
  </div>
  <p class="front-web">www.<span class="web-domain">harborlinecrest</span>.com</p>
</section>

<section class="card card-back">
  <div class="back-band" role="img" aria-label="Decorative blue and green wave band across the lower card"></div>

  <div class="rep">
    <h1 class="rep-name">Peter <span class="rep-surname">Vance</span></h1>
    <p class="rep-title">CEO/ Founder</p>
  </div>

  <p class="back-company">Harborline Crest Consulting</p>

  <ul class="contacts">
    <li>
      <svg viewBox="0 0 16 16"><path d="M3.5 1 L6 3.5 L4.6 5.6 C5.5 7.6 8.4 10.5 10.4 11.4 L12.5 10 L15 12.5 L13 15 C7 14.5 1.5 9 1 3 Z"/></svg>
      833-555-0172
    </li>
    <li>
      <svg viewBox="0 0 16 16"><path d="M1 3 H15 V13 H1 Z M2.5 4.5 L8 8.5 L13.5 4.5 Z" fill-rule="evenodd"/></svg>
      pvance@harborlinecrest.com
    </li>
    <li>
      <svg viewBox="0 0 16 16"><circle cx="8" cy="8" r="7"/><path d="M1 8 H15 M8 1 C5 4 5 12 8 15 M8 1 C11 4 11 12 8 15" stroke="#0a7dc7" stroke-width="1.2" fill="none"/></svg>
      www.harborlinecrest.com
    </li>
  </ul>
</section>

</body>
</html>
```